Brannock Bay Ferry and Haulage

Need to redesign our business cards to relay that we do freight logistics and water taxi service. We also work with gov. agencies doing environmental clean up, oil spill response, remote site construction and work with many of the air taxi and helicopter services on Kodiak Island. Out website is www.brannockbayferry.com to get a better idea of what we do.

Contact Information for Business Card

I have a previous business card but it just has the logo on the front, and a sunset picture on the back with the contact info. It does not relay what we do and what we can help with. I like a simple straight forward design over a busy one.

Colors
3176b5
0455a3
cfdfed

Requirements
Must have
• logo, email, website, phone number

```html
<!DOCTYPE html>
<html lang="en">
<head>
<meta charset="utf-8">
<title>Brannock Bay Ferry and Haulage – Business Card</title>
<link rel="stylesheet" href="https://fonts.googleapis.com/css2?family=Montserrat:wght@400;500;600;700&display=swap">
<style>
  :root {
    --page-bg: #d9d9d9;
    --card-bg: #efefee;
    --band-blue: #5bb3e0;
    --navy: #1f3d99;
    --orange: #f39c1f;
    --text-gray: #555555;
    --text-white: #ffffff;
    --divider: #b9b9b9;
  }
  * { margin: 0; padding: 0; box-sizing: border-box; }
  html, body {
    width: 1200px; height: 1200px; overflow: hidden;
    background: var(--page-bg);
    font-family: "Montserrat", sans-serif;
  }
  .card {
    position: absolute; left: 226px; width: 780px; height: 452px;
    background: var(--card-bg);
    overflow: hidden;
  }
  .card--front { top: 106px; }
  .card--back { top: 638px; }

  /* brand wordmark */
  .brand { position: absolute; display: flex; align-items: center; gap: 16px; }
  .brand__dot { width: 34px; height: 34px; border-radius: 50%; background: var(--orange); flex: none; }
  .brand__name {
    color: var(--navy); font-weight: 700; font-size: 30px; line-height: 1.15;
  }
  .card--front .brand { left: 0; right: 0; top: 108px; justify-content: center; }

  .service-band {
    position: absolute; left: 0; right: 0; top: 254px; bottom: 0;
    background: var(--band-blue); text-align: center;
  }
  .service-band__title {
    margin-top: 43px; color: var(--navy); font-weight: 700; font-size: 19px;
  }
  .service-list {
    list-style: none; display: flex; justify-content: center; flex-wrap: wrap;
    column-gap: 32px; row-gap: 14px; margin: 30px auto 0; width: 700px;
    color: var(--text-white); font-size: 19px; font-weight: 400; letter-spacing: 0.3px;
  }
  .service-list li { display: flex; align-items: center; gap: 6px; }
  .service-list li::before {
    content: ""; width: 10px; height: 10px; border-radius: 50%; background: var(--orange);
  }

  .card--back .brand {
    left: 40px; width: 330px; top: 176px; flex-direction: column; gap: 14px; text-align: center;
  }
  .card--back .brand__name { font-size: 28px; }
  .divider {
    position: absolute; left: 389px; top: 114px; width: 1px; height: 220px; background: var(--divider);
  }
  .contact { position: absolute; left: 420px; top: 110px; color: var(--text-gray); }
  .contact__name { color: var(--navy); font-weight: 600; font-size: 27px; letter-spacing: 0.5px; }
  .contact__role { color: var(--orange); font-size: 18px; margin-top: 2px; }
  .contact__address { font-size: 18px; line-height: 29px; margin-top: 26px; }
  .contact__lines { font-size: 18px; line-height: 26px; margin-top: 18px; }
  .contact__label { color: var(--orange); font-weight: 600; }
  .contact__web-name { color: var(--navy); }
</style>
</head>
<body>
  <section class="card card--front">
    <div class="brand">
      <span class="brand__dot"></span>
      <span class="brand__name">Brannock Bay Ferry and Haulage</span>
    </div>
    <div class="service-band">
      <h2 class="service-band__title">Freight logistics and water taxi service</h2>
      <ul class="service-list">
        <li>environmental clean up</li>
        <li>remote site constraction</li>
        <li>eco tourism</li>
        <li>oil spill response</li>
        <li>much more</li>
      </ul>
    </div>
  </section>

  <section class="card card--back">
    <div class="brand">
      <span class="brand__dot"></span>
      <span class="brand__name">Brannock Bay Ferry and Haulage</span>
    </div>
    <div class="divider"></div>
    <div class="contact">
      <h1 class="contact__name">OWEN HARTLEY</h1>
      <p class="contact__role">Owner</p>
      <p class="contact__address">240 Harbor Line Rd., Suite 12<br>Alaska, Brannock Island</p>
      <p class="contact__lines">
        <span class="contact__label">P</span>: 907-555-0182<br>
        <span class="contact__label">E</span>: brannockbayferry@gmail.com<br>
        <span class="contact__label">w</span>: www.<span class="contact__web-name">brannockbayferry</span>.com
      </p>
    </div>
  </section>
</body>
</html>
```